Brindel's Coating & Renewal Letterhead Design We want to revamp out old traditional letterhead with the new logo designs that are attached. We are working on getting all our company items from vehicles, business, cards, t-shirts, letterhead to match. This should include company colors, fonts, and flow of items that we have attached below.

Industry/Entity Type

Construction Company

Font styles to use
Sans Serif
Other font styles liked:
• Bold with outline

Colors
ec1f27
ffffff

Requirements
Must have
• Company Name: Brindel's Coating & Renewal
• Address: 4217 SW 83rd Ter Marlow Cove fl 33418
• Office Number: (954) 555-0194
• Email: Brindelrenewal@quorvane.com
• License Number: CGC8064392
Nice to have
• Company Colors: red, white, black, and grey

```html
<!DOCTYPE html>
<html lang="en">
<head>
<meta charset="utf-8">
<title>Brindel's Coating & Renewal — Letterhead</title>
<link href="https://fonts.googleapis.com/css2?family=Montserrat:wght@400;600;700&display=swap" rel="stylesheet">
<style>
  :root {
    --brand-red: #ec1f27;
    --accent-red: #e8462a;
    --ink: #333333;
    --swoosh-grey: #e6e6e6;
    --swoosh-pink: #fbd9d0;
    --rule-grey: #ececec;
    --backdrop: #e5e5e5;
    --paper: #ffffff;
  }
  * { margin: 0; padding: 0; box-sizing: border-box; }
  html, body { width: 1200px; height: 1200px; overflow: hidden; }
  body {
    background: var(--backdrop);
    font-family: "Montserrat", sans-serif;
    color: var(--ink);
    position: relative;
  }
  .letterhead {
    position: absolute;
    left: 262px; top: 122px;
    width: 676px; height: 956px;
    background: var(--paper);
    overflow: hidden;
  }
  .swooshes { position: absolute; left: 0; top: 0; width: 676px; height: 956px; }
  .top-rule {
    position: absolute; left: 0; top: 18px;
    width: 100%; height: 3px;
    background: var(--brand-red);
  }
  .company-name {
    position: absolute; left: 40px; top: 42px;
    width: 240px;
    font-weight: 700; font-size: 22px; line-height: 24px;
    text-transform: uppercase;
    color: var(--accent-red);
    letter-spacing: 0.5px;
  }
  .address {
    position: absolute; right: 41px; top: 78px;
    text-align: right;
    font-weight: 700; font-size: 14.5px; line-height: 17px;
  }
  .margin-rule {
    position: absolute; left: 95px; top: 170px;
    width: 1px; height: 611px;
    background: var(--rule-grey);
  }
  .signoff { position: absolute; left: 127px; top: 191px; }
  .signoff .closing { font-size: 11px; }
  .signoff .signer { margin-top: 12px; font-weight: 700; font-size: 19px; line-height: 20px; letter-spacing: 0.3px; }
  .signoff .role { font-weight: 700; font-size: 13.5px; line-height: 16px; }
  .body-copy {
    position: absolute; left: 127px;
    width: 520px;
    font-size: 11.1px; line-height: 22.3px;
    white-space: nowrap;
  }
  .p1 { top: 365px; }
  .p2 { top: 543px; }
  .p3 { top: 654px; }
  .phone {
    position: absolute; left: 38px; top: 654px;
    width: 20px; height: 130px;
  }
  .phone-number {
    position: absolute; left: 0; bottom: 22px;
    transform-origin: left bottom;
    transform: rotate(-90deg) translate(0, 18px);
    font-weight: 700; font-size: 13.6px; white-space: nowrap;
  }
  .phone-icon { position: absolute; left: 2px; bottom: 0; width: 16px; height: 16px; }
  .license {
    position: absolute; left: 41px; top: 900px;
    font-weight: 700; font-size: 13.6px;
  }
  .contact { position: absolute; left: 421px; top: 886px; }
  .contact-line { display: flex; align-items: center; gap: 6px; height: 15.5px; font-weight: 700; font-size: 13.4px; }
  .contact-line svg { width: 14px; height: 14px; flex: none; }
</style>
</head>
<body>
  <main class="letterhead">
    <svg class="swooshes" viewBox="0 0 676 956" aria-hidden="true">
      <path fill="var(--swoosh-grey)" d="M0,222 C250,205 480,120 622,0 L582,0 C450,105 230,188 0,208 Z"/>
      <path fill="var(--swoosh-grey)" d="M400,169 C520,140 620,100 676,64 L676,22 C590,88 500,135 400,169 Z"/>
      <path fill="var(--swoosh-pink)" d="M155,956 C230,920 310,900 395,879 C340,900 270,925 215,956 Z"/>
      <path fill="var(--swoosh-pink)" d="M395,956 C480,915 580,895 672,879 C600,900 520,925 460,956 Z"/>
    </svg>

    <div class="top-rule"></div>

    <h1 class="company-name">Brindel's<br>Coating &amp;<br>Renewal</h1>

    <address class="address">4217 SW 83rd Ter Marlow Cove<br>fl 33418</address>

    <div class="margin-rule"></div>

    <section class="signoff">
      <p class="closing">Sincearly,</p>
      <p class="signer">DANA MERROW</p>
      <p class="role">Director</p>
    </section>

    <p class="body-copy p1">This is a sample letter that has been placed to demonstrate typing remat (Your Company).<br>letterhead design. When positioned properly, it will serve to work in harmony with all other<br>elements letterhead. This letterhead design is meant to project an image<br>This letterhead design is meant project an image of professionalism reliability. By using<br>simple aligen we have created a very spacious feeling. The simplicity suggest &nbsp;rengththe<br>spaciousnes contributes haesthetics the layout. These basic qualities along with the<br>(Your Company)</p>

    <p class="body-copy p2">look and helps reinforce the (Your Company) brand. letterhead design is meant to project<br>an image design. When positioned properly, it will serve to work in harmony all the other<br>elements letterhead. sionalism and reliability.</p>

    <p class="body-copy p3">This letterhead design is based on the (Form of your logo) form (Your Company) logo.<br>Each stationery we have created a very spacious feeling. The simplicity suggests strength<br>the spaciousnes contribute part of the (Form of your logo).<br>This letterhead design is based on the (Form of your logo) form (Your Company) logo.<br>Each stationery we have created a very spacious feeling. The simplicity suggests strength<br>the spaciousnes contribute part of the (Form of your logo).</p>

    <div class="phone">
      <span class="phone-number">(954) 555-0194</span>
      <svg class="phone-icon" viewBox="0 0 16 16" aria-hidden="true">
        <circle cx="8" cy="8" r="7" fill="none" stroke="var(--accent-red)" stroke-width="1.2"/>
        <path d="M5.5 5 C5 7.5 7.5 10.8 10.8 10.5 L11 9.4 L9.6 8.8 L9 9.5 C8 9 7 8 6.6 7 L7.3 6.4 L6.7 5 Z" fill="var(--accent-red)"/>
      </svg>
    </div>

    <p class="license">License Number: CGC8064392</p>

    <div class="contact">
      <p class="contact-line">
        <svg viewBox="0 0 14 14" aria-hidden="true"><circle cx="7" cy="7" r="6.3" fill="none" stroke="var(--accent-red)" stroke-width="1"/><rect x="4" y="5" width="6" height="4.2" fill="var(--accent-red)"/><path d="M4 5 L7 7.3 L10 5" fill="none" stroke="#fff" stroke-width="0.7"/></svg>
        Brindelrenewal@quorvane.com
      </p>
      <p class="contact-line">
        <svg viewBox="0 0 14 14" aria-hidden="true"><circle cx="7" cy="7" r="6.3" fill="none" stroke="var(--accent-red)" stroke-width="1"/><circle cx="7" cy="7" r="3.6" fill="none" stroke="var(--accent-red)" stroke-width="0.8"/><ellipse cx="7" cy="7" rx="1.5" ry="3.6" fill="none" stroke="var(--accent-red)" stroke-width="0.7"/><path d="M3.4 7 H10.6" stroke="var(--accent-red)" stroke-width="0.7"/></svg>
        www.brindelrenewal
      </p>
    </div>
  </main>
</body>
</html>
```